Trondel Group letterhead

Hi,

I need a letterhead template created for our business. This should be done in word format and A4 size. The images need to not move in the template ie when I am adding writing in etc. and should flow on when I get to a second page.

I have attached our logo templates below.

Other details to include on the letterhead somewhere are:

0438 571 962
Max@Trondelelectrical.example.com.au
PO Box 781 Marrowdale NSW 2163
ABN: 57 318 492 076

Thanks!

```html
<!DOCTYPE html>
<html lang="en">
<head>
<meta charset="utf-8">
<title>Trondel Group Letterhead</title>
<link href="https://fonts.googleapis.com/css2?family=Montserrat:wght@400;800&family=Source+Sans+3:wght@400&display=swap" rel="stylesheet">
<style>
  :root {
    --backdrop: #e4e4e4;
    --paper: #ffffff;
    --ink: #2b2b2b;
    --ink-soft: #3a3a3a;
    --brand-orange: #ec5222;
    --brand-black: #1d1d1d;
  }
  * { margin: 0; padding: 0; box-sizing: border-box; }
  html, body {
    width: 1200px; height: 1079px; overflow: hidden;
    background: var(--backdrop);
  }
  .letterhead {
    position: absolute; left: 218px; top: 0;
    width: 763px; height: 1079px;
    background: var(--paper);
    color: var(--ink);
    font-family: "Source Sans 3", "Myriad Pro", sans-serif;
    overflow: hidden;
  }
  .brand {
    position: absolute; left: 72px; top: 96px;
    display: flex; align-items: center; gap: 12px;
  }
  .brand-dot {
    width: 30px; height: 30px; border-radius: 50%;
    background: var(--brand-orange);
  }
  .brand-name {
    font-family: "Montserrat", sans-serif;
    font-weight: 800; font-size: 26px; letter-spacing: 0.5px;
    color: var(--brand-black); text-transform: uppercase;
    white-space: nowrap;
  }
  .contact {
    position: absolute; right: 73px; top: 80px;
    font-family: "Montserrat", sans-serif; font-style: normal;
    font-size: 13px; line-height: 18px; color: var(--ink);
    white-space: nowrap;
  }
  .contact .label { color: var(--brand-orange); }
  .contact .gap { height: 14px; }
  .contact-line { display: flex; align-items: center; gap: 5px; }
  .contact-line svg { width: 11px; height: 11px; flex: none; }
  .recipient {
    position: absolute; left: 72px; top: 319px;
    line-height: 19px;
  }
  .recipient-name { font-size: 15.5px; text-transform: uppercase; color: var(--ink); }
  .recipient-detail { font-size: 11.5px; color: var(--ink-soft); }
  .letter-body {
    position: absolute; left: 72px; top: 462px; width: 618px;
    font-size: 11.2px; line-height: 18.8px; color: var(--ink-soft);
    text-align: justify;
  }
  .letter-body p + p { margin-top: 16px; }
  .closing {
    position: absolute; left: 72px; top: 852px;
    font-size: 12px; color: var(--ink);
  }
  .footer-band-dark {
    position: absolute; left: 0; bottom: 0; width: 65px; height: 14px;
    background: var(--brand-black);
  }
  .footer-band-accent {
    position: absolute; left: 71px; right: 0; bottom: 0; height: 14px;
    background: var(--brand-orange);
  }
</style>
</head>
<body>
  <main class="letterhead">
    <div class="brand">
      <span class="brand-dot"></span>
      <span class="brand-name">Trondel Group</span>
    </div>

    <address class="contact">
      <div>PO Box 781 Marrowdale NSW 2163</div>
      <div><span class="label">ABN:</span> 57 318 492 076</div>
      <div class="gap"></div>
      <div class="contact-line">
        <svg viewBox="0 0 24 24" aria-hidden="true"><path fill="#ec5222" d="M6.6 10.8a15.1 15.1 0 0 0 6.6 6.6l2.2-2.2c.3-.3.7-.4 1-.2 1.1.4 2.3.6 3.6.6.6 0 1 .4 1 1V20c0 .6-.4 1-1 1A17 17 0 0 1 3 4c0-.6.4-1 1-1h3.5c.6 0 1 .4 1 1 0 1.3.2 2.5.6 3.6.1.3 0 .7-.2 1z"/></svg>
        <span>0438 571 962</span>
      </div>
      <div class="contact-line">
        <svg viewBox="0 0 24 24" aria-hidden="true"><rect x="2" y="5" width="20" height="14" rx="2" fill="#ec5222"/><path d="M3 7l9 6 9-6" fill="none" stroke="#fff" stroke-width="2"/></svg>
        <span>Max@Trondelelectrical.example.com.au</span>
      </div>
    </address>

    <section class="recipient">
      <div class="recipient-name">Odette Varnum</div>
      <div class="recipient-detail">Chief Exective Officer</div>
      <div class="recipient-detail">City/State, Zip Code</div>
    </section>

    <section class="letter-body">
      <p>Proin gravida nibh vel velit auctor aliquet. Aenean sollicitudin, lorem quis bibendum auctor, nisi elit consequat ipsum, nec sagittis sem nibh id elit. Duis sed odio sit amet nibh vulputate cursus a sit amet mauris. Morbi accumsan ipsum velit. Nam nec tellus a odio tincidunt auctor a ornare odio. Sed non mauris vitae erat consequat auctor eu in elit. Class aptent taciti sociosqu imperdiet nisi. Proin condimentum fermentum nunc. Etiam pharetra, erat sed fermentum feugiat, velit mauris egestas quam, ut aliquam massa nisl quis neque. Suspendisse in orci enim.</p>
      <p>This is a standard version of Lorem Ipsum. Proin gravida nibh vel velit auctor aliquet. Aenean sollicitudin, lorem quis bibendum auctor, nisi elit consequat ipsum, nec sagittis sem nibh id elit. Duis sed odio sit amet nibh vulputate cursus a sit amet mauris. Mo rbi accumsan ipsum velit. Nam nec tellus a odio tincidunt auctor a ornare odio. Sed non mauris vitae erat consequat auctor eu in elit. Class aptt consequat auctor eu in elit. Class aptent taciti sociosqu ad litora torquent per conubia nostra, per inceptos himenaeos. Mauris in erat justo.</p>
      <p>Nullam ac urna eu felis dapibus condimentum sit amet a augue. Sed non neque elit. Sed ut imperdiet nisi. Proin condimentum fermentum nunc. Etiam pharetra, erat sed fermentum feugiat, velit mauris egestas quam.Nullam ac urna eu felis dapibus condimentum sit amet a aug pharetra, erat sed fermentum feugiat, velit mauris egestas quam.Nullam ac urna nunc. tum nunc. Etiam pharetra, erat sed fermentum feugiat, velit mauris egestas quam.Nullam ac urna eu felis dapibus condimentum sit amet a aug pharetra, erat sed fermentum feugiat, velit mauris egestas quam.Nullam ac urna eu felis dapibus condimentum sit amet a augue. Sed non</p>
    </section>

    <p class="closing">Sincerely,</p>

    <div class="footer-band-dark"></div>
    <div class="footer-band-accent"></div>
  </main>
</body>
</html>
```